Building company business card

Design and print business cards for BRENTHOLM PTY LTD.
A residantial homes building company.
Mark Lantern already designed the company Logo.

```html
<!DOCTYPE html>
<html lang="en">
<head>
<meta charset="utf-8">
<title>BRENTHOLM PTY LTD — Business Card</title>
<link rel="stylesheet" href="https://fonts.googleapis.com/css2?family=Montserrat:wght@400;500;600;700;800&display=swap">
<style>
  :root {
    --bg: #3a3a3c;
    --white: #ffffff;
    --navy: #10206a;
    --gold: #c8902e;
    --gold-light: #e8c26a;
    --ink: #1c1c1c;
  }
  * { box-sizing: border-box; margin: 0; padding: 0; }
  html, body { width: 1200px; height: 1200px; overflow: hidden; }
  body {
    background: var(--bg);
    font-family: "Montserrat", sans-serif;
    position: relative;
  }
  .card {
    position: absolute;
    left: 150px;
    width: 900px;
    height: 514px;
    border-radius: 34px;
    overflow: hidden;
  }
  .card-front { top: 60px; background: var(--white); }
  .card-back { top: 626px; background: var(--navy); }

  .contact-block {
    position: absolute;
    left: 70px;
    top: 178px;
    color: var(--ink);
  }
  .person-name {
    font-size: 34px;
    font-weight: 600;
    color: var(--gold);
    letter-spacing: 1px;
    line-height: 1;
    white-space: nowrap;
  }
  .person-role {
    font-size: 17px;
    font-weight: 500;
    letter-spacing: 1px;
    margin-top: 6px;
  }
  .contact-list { list-style: none; margin-top: 28px; }
  .contact-list li {
    display: flex;
    align-items: flex-start;
    font-size: 20px;
    line-height: 1.25;
    margin-bottom: 6px;
  }
  .contact-icon { width: 22px; height: 22px; margin-right: 14px; margin-top: 2px; flex: none; }
  .registry {
    margin: 16px 0 0 36px;
    font-size: 19px;
    line-height: 1.25;
  }

  .brand-mark {
    position: absolute;
    display: flex;
    align-items: center;
    font-weight: 800;
    letter-spacing: 2px;
    line-height: 1;
    white-space: nowrap;
  }
  .brand-mark .mark-square { background: var(--gold); flex: none; }
  .card-front .brand-mark {
    right: 70px;
    top: 84px;
    font-size: 44px;
    color: var(--navy);
  }
  .card-front .mark-square { width: 32px; height: 32px; margin-right: 16px; }
  .card-back .brand-mark {
    left: 50%;
    top: 50%;
    transform: translate(-50%, -50%);
    font-size: 82px;
    color: var(--white);
  }
  .card-back .mark-square { width: 60px; height: 60px; margin-right: 28px; }

  .gold-band {
    position: absolute;
    left: 420px;
    bottom: 0;
    width: 340px;
    height: 28px;
    background: linear-gradient(90deg, var(--gold), var(--gold-light) 50%, var(--gold));
  }
</style>
</head>
<body>
  <section class="card card-front">
    <div class="brand-mark"><span class="mark-square"></span>BRENTHOLM</div>

    <div class="contact-block">
      <h1 class="person-name">DORIAN (DEE) CASTELL</h1>
      <p class="person-role">DIRECTOR</p>
      <ul class="contact-list">
        <li>
          <svg class="contact-icon" viewBox="0 0 24 24"><path fill="#c8902e" d="M6.6 10.8a15.1 15.1 0 0 0 6.6 6.6l2.2-2.2c.3-.3.7-.4 1-.2 1.1.4 2.3.6 3.6.6.6 0 1 .4 1 1V20c0 .6-.4 1-1 1A17 17 0 0 1 3 4c0-.6.4-1 1-1h3.5c.6 0 1 .4 1 1 0 1.3.2 2.5.6 3.6.1.3 0 .7-.2 1z"/></svg>
          0400 555 812
        </li>
        <li>
          <svg class="contact-icon" viewBox="0 0 24 24"><path fill="#c8902e" d="M2 5h20v14H2z"/><path fill="none" stroke="#fff" stroke-width="1.6" d="M2.5 5.5 12 13l9.5-7.5"/></svg>
          dcl@brentholm-pl.com
        </li>
        <li>
          <svg class="contact-icon" viewBox="0 0 24 24"><path fill="#c8902e" d="M12 2a7 7 0 0 0-7 7c0 5.2 7 13 7 13s7-7.8 7-13a7 7 0 0 0-7-7zm0 9.5a2.5 2.5 0 1 1 0-5 2.5 2.5 0 0 1 0 5z"/></svg>
          <span>BRENTHOLM PTY LTD<br>PO Box 248 Elmwood East Vic 3999</span>
        </li>
      </ul>
      <p class="registry">ABN- 48 120 556 902<br>CDB-U 51840</p>
    </div>

    <div class="gold-band"></div>
  </section>

  <section class="card card-back">
    <div class="brand-mark"><span class="mark-square"></span>BRENTHOLM</div>
  </section>
</body>
</html>
```